VerdantMed Business Card & Stationary
VerdantMed Pharmacy
VerdantMed Business Card & Stationary - Pharmacy/Pharmaceuticals
Creative Brief
Professional
Clara J Vandermeer RPh
Owner/Pharmacist
3870 FM 2209 Rd, Suite 200, Katy, TX 77495
555-010-0147 Can use any 10 numbers for illustration purposes
clara@verdantmed-example.com
www.verdantmed-example.com
We are looking for something very stylish and creative yet professional that will capture attention and reinforce our branding strategy efforts. We would also like to have the ability with whatever digital files are sent to us to be easily changed by printing company to so that we could interchange staff members names and titles on the business cards. Please use modern symbols for phone, mobile, fax, web. No QR code needed. Would like to see the drafts using the logo color variations (silver or gold or blue and gray/silver) in the logo upload files. Thank you.
Designers Creativity. Editable Fields - need to be able to modify and list the pharmacy's services that will be offered: Willow Health Clinic Quick and Convenient Drive Thru Compounding: Traditional, Specialty, Pet Immunizations and Health Screening Delivery
belvuto belvuto
Project is Unveiled. Looking forward to your work towards refining the cards. Thank you.

```html
<!DOCTYPE html>
<html lang="en">
<head>
<meta charset="utf-8">
<title>VerdantMed Pharmacy Stationery</title>
<link rel="stylesheet" href="https://fonts.googleapis.com/css2?family=Cormorant+Garamond:wght@500;600&family=Lato:wght@400;700&display=swap">
<style>
  :root {
    --ground: #ece4d6;
    --paper: #ffffff;
    --teal: #7fa2a5;
    --teal-deep: #5d8589;
    --teal-soft: #c9dadb;
    --brown: #5a3f2b;
    --gold: #b59a6a;
    --ink: #5b6264;
    --seal: #a3161b;
    --shadow: rgba(60, 45, 25, .25);
  }
  * { box-sizing: border-box; margin: 0; padding: 0; }
  html, body { width: 1200px; height: 271px; overflow: hidden; }
  body {
    background: var(--ground);
    font-family: "Lato", sans-serif;
    color: var(--ink);
    position: relative;
  }
  .piece {
    position: absolute;
    background: var(--paper);
    box-shadow: 1px 2px 4px var(--shadow);
    overflow: hidden;
  }
  .brand {
    font-family: "Cormorant Garamond", serif;
    font-weight: 600;
    color: var(--teal-deep);
    letter-spacing: .3px;
    white-space: nowrap;
  }
  .art {
    position: absolute;
    background: radial-gradient(ellipse at center, var(--teal-soft) 0%, rgba(201,218,219,0) 70%);
  }
  .band { position: absolute; left: 0; right: 0; background: linear-gradient(90deg, var(--teal-deep), var(--teal)); }

  /* business cards */
  .card-front { left: 14px; top: 70px; width: 130px; height: 74px; background: linear-gradient(135deg, #fbf8f2, #efe6d4); }
  .card-front .brand { position: absolute; left: 10px; top: 8px; font-size: 15px; color: var(--gold); }
  .card-front .person { position: absolute; left: 10px; top: 30px; font-size: 5.5px; line-height: 7px; color: var(--brown); }
  .card-front .person b { font-size: 6.5px; }
  .card-front .contact { position: absolute; right: 8px; bottom: 6px; font-size: 4.5px; line-height: 6px; text-align: right; color: var(--brown); white-space: nowrap; }
  .card-back { left: 14px; top: 156px; width: 130px; height: 74px; background: linear-gradient(135deg, var(--brown), #3c2a1c); }
  .card-back .art { left: 60px; top: 8px; width: 66px; height: 58px; background: radial-gradient(ellipse, var(--gold), rgba(181,154,106,0) 70%); }
  .card-back .brand { position: absolute; left: 10px; top: 28px; font-size: 14px; color: var(--gold); }

  /* letterhead */
  .letterhead { left: 160px; top: 14px; width: 185px; height: 240px; }
  .letterhead .brand { position: absolute; left: 0; right: 0; top: 14px; text-align: center; font-size: 14px; }
  .letterhead .art { left: 45px; top: 128px; width: 100px; height: 84px; }
  .letterhead .body { position: absolute; left: 18px; right: 18px; top: 50px; font-size: 5px; line-height: 8px; }
  .letterhead .band { bottom: 14px; height: 12px; }
  .letterhead .foot { position: absolute; left: 0; right: 0; bottom: 4px; text-align: center; font-size: 4px; color: var(--teal-deep); white-space: nowrap; }

  /* CD */
  .disc { left: 358px; top: 12px; width: 124px; height: 124px; border-radius: 50%; background: radial-gradient(circle, var(--ground) 0 9px, #d9d9d9 10px 20px, #fff 21px); box-shadow: 1px 2px 4px var(--shadow); position: absolute; }
  .disc .brand { position: absolute; left: 0; right: 0; top: 28px; text-align: center; font-size: 12px; }
  .disc .art { left: 22px; top: 80px; width: 80px; height: 30px; }

  /* compliment card & seal */
  .note { left: 495px; top: 96px; width: 200px; height: 56px; }
  .note .brand { position: absolute; left: 0; right: 0; top: 16px; text-align: center; font-size: 14px; }
  .note .band { bottom: 0; height: 8px; }
  .seal { position: absolute; left: 600px; top: 20px; width: 46px; height: 46px; border-radius: 50%; background: radial-gradient(circle at 40% 35%, #d43a3a, var(--seal) 60%, #6d0c10); box-shadow: 1px 2px 4px var(--shadow); }

  /* envelopes */
  .env-window { left: 360px; top: 170px; width: 190px; height: 84px; }
  .env-window .brand { position: absolute; left: 10px; top: 8px; font-size: 10px; }
  .env-window .window { position: absolute; left: 70px; top: 40px; width: 90px; height: 26px; border: 1px solid #cfd6d7; border-radius: 3px; font-size: 5px; line-height: 7px; padding: 2px 5px; }
  .env-window .band { bottom: 0; height: 6px; }
  .env-flap { left: 565px; top: 170px; width: 195px; height: 84px; }
  .env-flap svg { position: absolute; inset: 0; }
  .env-flap .brand { position: absolute; left: 0; right: 0; top: 50px; text-align: center; font-size: 11px; }

  /* catalog envelope */
  .env-tall { left: 775px; top: 14px; width: 180px; height: 240px; }
  .env-tall svg { position: absolute; left: 0; top: 0; }
  .env-tall .brand { position: absolute; left: 12px; top: 60px; font-size: 13px; }
  .env-tall .band { bottom: 20px; height: 10px; }

  /* folder */
  .folder { left: 970px; top: 14px; width: 218px; height: 240px; }
  .folder svg { position: absolute; inset: 0; }
  .folder .art { left: 40px; top: 90px; width: 120px; height: 110px; }
  .folder .brand { position: absolute; right: 6px; top: 60px; font-size: 20px; writing-mode: vertical-rl; }
  .folder .band { bottom: 0; height: 10px; }
</style>
</head>
<body>

<div class="piece card-front">
  <div class="brand">VerdantMed</div>
  <div class="person"><b>Clara J Vandermeer RPh</b><br>Owner/Pharmacist</div>
  <div class="contact">48 Larkspur Lane, Suite 12, Fernvale<br>555-010-0147 · clara@verdantmed-example.com<br>www.verdantmed-example.com</div>
</div>
<div class="piece card-back">
  <div class="art" role="img" aria-label="Mortar and pestle illustration"></div>
  <div class="brand">VerdantMed</div>
</div>

<div class="piece letterhead">
  <div class="brand">VerdantMed</div>
  <div class="art" role="img" aria-label="Faint leaf and mortar watermark illustration"></div>
  <div class="body">
    Dear Client,<br><br>
    Thank you for choosing our pharmacy for your care.<br>
    We look forward to serving you and your family.<br><br>
    Sincerely,<br><br>
    Clara J Vandermeer RPh
  </div>
  <div class="band"></div>
  <div class="foot">48 Larkspur Lane, Suite 12, Fernvale · www.verdantmed-example.com</div>
</div>

<div class="disc">
  <div class="brand">VerdantMed</div>
  <div class="art" role="img" aria-label="Leaf illustration"></div>
</div>

<div class="seal" role="img" aria-label="Red wax seal"></div>

<div class="piece note">
  <div class="brand">VerdantMed</div>
  <div class="band"></div>
</div>

<div class="piece env-window">
  <div class="brand">VerdantMed</div>
  <div class="window">Recipient Name<br>Street Address<br>City, State Zip</div>
  <div class="band"></div>
</div>

<div class="piece env-flap">
  <svg width="195" height="84" viewBox="0 0 195 84">
    <polyline points="0,0 97.5,42 195,0" fill="none" stroke="#c9dadb" stroke-width="1.5"/>
    <rect x="0" y="78" width="195" height="6" fill="#7fa2a5"/>
  </svg>
  <div class="brand">VerdantMed</div>
</div>

<div class="piece env-tall">
  <svg width="180" height="240" viewBox="0 0 180 240">
    <polyline points="0,0 90,36 180,0" fill="none" stroke="#c9dadb" stroke-width="1.5"/>
  </svg>
  <div class="brand">VerdantMed</div>
  <div class="band"></div>
</div>

<div class="piece folder">
  <svg width="218" height="240" viewBox="0 0 218 240">
    <polygon points="0,150 150,150 218,200 218,240 0,240" fill="#f4f7f7" stroke="#c9dadb"/>
  </svg>
  <div class="art" role="img" aria-label="Large faint mortar and leaf illustration"></div>
  <div class="brand">VerdantMed</div>
  <div class="band"></div>
</div>

</body>
</html>
```